'Under Cold Glass' Thriller Movie Poster

Oaklume Pictures would like a poster design for their film 'Under Cold Glass'. It is a psychological thriller told through the eyes of Lulu Penrose - a C list celebrity - who will do anything to keep her name in the press.

After a nightclub appearance, she gets kidnapped and wakes up in a basement, who holds her hostage for ransom money. Lulu tries to use her fame to help raise the money, but gets caught up in a web of lies and scandal.

The director envisages a close-up of Lulu in the basement, with only one side of her face lit. I have uploaded a few screen grabs and a wide shot which has a more expressive look if that works for your design better.

We want something eye-catchy and to fit the mood of the film.

Thank you for your time in advance.

Industry/Entity Type

Movie

Requirements
Must have
• Information at the bottom of the poster in the usually tall white font...
• A OAKLUME PICTURES Production
• Starring GRAHAM OSTLER NADIA CROWLEY PATRICIA FLINT DORIANE HOLT with FREDERICK MAROSI and CAROL DUNFEE
• Make Up & Hair by MAEVE ROCKWOOD Wardrobe TESSA HOLLOWAY Editor OSWALD TER HOUVEN Supervising Editor ANDERS PELTONEN Art Director DESMOND QUAYLE Music NIAMH FORBES Director of Photography TOBIAS HARTUNG
• Executive Producers OWAIN PRICHARD HOLLIE PRICHARD KIT MERCERON and RAVI DESAI Production Manager GENEVIEVE CROWLEY-PASK Associate Producer CONOR BLYTHE
• Screenplay by EDWIN FAULKNER-DEKKER & BARNABY COLT Directed by BARNABY COLT
• In the main body of the poster - the title 'UNDER COLD GLASS'.

```html
<!DOCTYPE html>
<html lang="en">
<head>
<meta charset="utf-8">
<title>Under Cold Glass – Poster</title>
<link rel="stylesheet" href="https://fonts.googleapis.com/css2?family=Bebas+Neue&family=League+Gothic&display=swap">
<style>
  :root {
    --bg: #000000;
    --title-bright: #d8481a;
    --title-dim: #8a2e14;
    --credit: #e8e4df;
    --photo-light: #b9b08a;
    --photo-mid: #5b5a3e;
    --photo-dark: #1a1510;
  }
  * { margin: 0; padding: 0; box-sizing: border-box; }
  html, body {
    width: 790px; height: 1200px; overflow: hidden; background: var(--bg);
  }
  .poster {
    position: relative; width: 790px; height: 1200px; overflow: hidden;
    background: var(--bg);
  }
  .key-art {
    position: absolute; left: 20px; top: 0; width: 760px; height: 1000px;
    background:
      radial-gradient(ellipse 220px 280px at 430px 470px, rgba(200,190,150,0.6), transparent 70%),
      radial-gradient(ellipse 110px 130px at 180px 620px, rgba(210,200,170,0.45), transparent 75%),
      radial-gradient(ellipse 380px 490px at 400px 430px, var(--photo-mid), var(--photo-dark) 72%, transparent 100%);
    opacity: 0.9;
  }
  .title-stack {
    position: absolute; left: 0; top: 0; width: 790px; height: 1000px;
  }
  .title-stack text {
    font-family: 'Bebas Neue', 'League Gothic', sans-serif;
    font-size: 193px;
  }
  .title-line--echo { fill: var(--title-dim); fill-opacity: 0.75; }
  .title-line--main { fill: var(--title-bright); }
  .credits {
    position: absolute; left: 0; top: 1040px; width: 790px;
    text-align: center; color: var(--credit);
    font-family: 'League Gothic', 'Bebas Neue', sans-serif;
    line-height: 13px; letter-spacing: 0.2px;
  }
  .credits p { font-size: 12.5px; white-space: nowrap; }
  .credits .role { font-size: 7.5px; letter-spacing: 0.4px; margin: 0 2px; }
</style>
</head>
<body>
<main class="poster">
  <div class="key-art" role="img" aria-label="Dark, moody key-art photograph: a half-lit close-up seen through cracked glass"></div>

  <svg class="title-stack" viewBox="0 0 790 1000" aria-label="Under Cold Glass">
    <text class="title-line--echo" x="66" y="165" textLength="657" lengthAdjust="spacingAndGlyphs">UNDER COLD GLASS</text>
    <text class="title-line--echo" x="66" y="311" textLength="657" lengthAdjust="spacingAndGlyphs">UNDER COLD GLASS</text>
    <text class="title-line--echo" x="66" y="457" textLength="657" lengthAdjust="spacingAndGlyphs">UNDER COLD GLASS</text>
    <text class="title-line--echo" x="66" y="603" textLength="657" lengthAdjust="spacingAndGlyphs">UNDER COLD GLASS</text>
    <text class="title-line--echo" x="66" y="749" textLength="657" lengthAdjust="spacingAndGlyphs">UNDER COLD GLASS</text>
    <text class="title-line--main" x="66" y="895" textLength="657" lengthAdjust="spacingAndGlyphs">UNDER COLD GLASS</text>
  </svg>

  <section class="credits">
    <p><span class="role">A</span>OAKLUME PICTURES<span class="role">PRODUCTION</span> 'UNDER COLD GLASS' <span class="role">STARRING</span>GRAHAM OSTLER &nbsp;NADIA CROWLEY &nbsp;PATRICIA FLINT &nbsp;DORIANE HOLT <span class="role">WITH</span>FREDERICK MAROSI <span class="role">AND</span>CAROL DUNFEE</p>
    <p><span class="role">MAKE UP &amp; HAIR</span>MAEVE ROCKWOOD <span class="role">WARDROBE</span>TESSA HOLLOWAY</p>
    <p><span class="role">EDITED BY</span>OSWALD TER HOUVEN <span class="role">SUPERVISING EDITOR</span>ANDERS PELTONEN <span class="role">ART DIRECTOR</span>DESMOND QUAYLE <span class="role">MUSIC</span>NIAMH FORBES</p>
    <p><span class="role">DIRECTOR OF PHOTOGRAPHY</span>TOBIAS HARTUNG <span class="role">EXECUTIVE PRODUCERS</span>OWAIN PRICHARD &nbsp;HOLLIE PRICHARD &nbsp;KIT MERCERON <span class="role">AND</span>RAVI DESAI</p>
    <p><span class="role">PRODUCTION MANAGER</span>GENEVIEVE CROWLEY-PASK <span class="role">ASSOCIATE PRODUCER</span>CONOR BLYTHE</p>
    <p><span class="role">SCREENPLAY BY</span>EDWIN FAULKNER-DEKKER &amp; BARNABY COLT <span class="role">DIRECTED BY</span>BARNABY COLT</p>
  </section>
</main>
</body>
</html>
```